Business Card Design Project

I need a business card for an environmentally friendly interior design company called Maplecrest Decor.
I was thinking it might be nice to print the business cards on brown recycled paper with green ink.
In addition to interior design, I will also be able to consult with homeowners regarding their indoor environments and how they might be affecting their health after May 2013 which is when I will complete my certification program. This can be added to the business card at that time: "Certified Dwelling Vitality Environmental Consultant".

```html
<!DOCTYPE html>
<html lang="en">
<head>
<meta charset="utf-8">
<title>Maplecrest Decor — Business Card</title>
<link href="https://fonts.googleapis.com/css2?family=Questrial&family=Arimo:wght@400&display=swap" rel="stylesheet">
<style>
  :root {
    --bg: #efece6;
    --kraft: #d6cfbf;
    --band: #dcdbcc;
    --ink: #14923f;
    --shadow: rgba(60, 45, 25, 0.22);
  }
  * { margin: 0; padding: 0; box-sizing: border-box; }
  html, body {
    width: 1200px; height: 900px; overflow: hidden;
    background: var(--bg);
  }
  .stage {
    position: relative; width: 1200px; height: 900px;
  }
  .card {
    position: absolute; left: 320px;
    width: 560px; height: 320px;
    background: var(--kraft);
    box-shadow: 0 6px 18px var(--shadow);
    color: var(--ink);
    overflow: hidden;
  }
  .card--front { top: 110px; }
  .card--back  { top: 470px; }

  .band {
    position: absolute;
    background: var(--band);
  }
  .card--front .band { left: 0; top: 186px; width: 530px; height: 104px; }
  .card--back  .band { left: 0; top: 196px; width: 536px; height: 94px; }

  .accent-bar {
    position: absolute; width: 9px; background: var(--ink);
  }
  .card--front .accent-bar { left: 0; top: 186px; height: 42px; }
  .card--back  .accent-bar { left: 536px; top: 248px; height: 42px; }

  .contact {
    position: absolute; left: 44px; top: 40px;
    font-family: "Arimo", Arial, sans-serif;
  }
  .contact__name { font-size: 19px; line-height: 1.2; }
  .contact__phone {
    display: flex; align-items: center; gap: 8px;
    font-size: 15px; margin-top: 4px;
  }
  .contact__phone svg { width: 11px; height: 13px; margin-left: -19px; }

  .wordmark {
    position: absolute;
    font-family: "Questrial", "Century Gothic", sans-serif;
    white-space: nowrap;
  }
  .card--front .wordmark { right: 40px; top: 128px; font-size: 36px; }
  .card--back  .wordmark { right: 52px; top: 220px; font-size: 40px; }

  .services {
    position: absolute; left: 26px; top: 196px;
    font-family: "Arimo", Arial, sans-serif;
    font-size: 14.5px; line-height: 1.38;
    list-style: none;
  }
</style>
</head>
<body>
<main class="stage">
  <section class="card card--front" aria-label="Business card front">
    <div class="band"></div>
    <div class="accent-bar"></div>
    <div class="contact">
      <p class="contact__name">Dana Rowe Ellis</p>
      <p class="contact__phone">
        <svg viewBox="0 0 11 13" aria-hidden="true">
          <rect x="0.6" y="0.6" width="9.8" height="11.8" rx="1.2" fill="none" stroke="currentColor" stroke-width="1.2"/>
          <rect x="2.5" y="2.5" width="6" height="3" fill="currentColor"/>
          <rect x="2.5" y="7" width="1.6" height="1.4" fill="currentColor"/>
          <rect x="4.7" y="7" width="1.6" height="1.4" fill="currentColor"/>
          <rect x="6.9" y="7" width="1.6" height="1.4" fill="currentColor"/>
          <rect x="2.5" y="9.2" width="1.6" height="1.4" fill="currentColor"/>
          <rect x="4.7" y="9.2" width="1.6" height="1.4" fill="currentColor"/>
          <rect x="6.9" y="9.2" width="1.6" height="1.4" fill="currentColor"/>
        </svg>
        (555) 318-4072
      </p>
    </div>
    <p class="wordmark">Maplecrest Decor</p>
    <ul class="services">
      <li>Maplecrest Decor</li>
      <li>Environmentally friendly design</li>
      <li>Certified Dwelling Vitality Environmental Consultant</li>
    </ul>
  </section>

  <section class="card card--back" aria-label="Business card back">
    <div class="band"></div>
    <div class="accent-bar"></div>
    <p class="wordmark">Maplecrest Decor</p>
  </section>
</main>
</body>
</html>
```